Apply Existing Website Design to Pellmoor-Made Tele-Wellness App (UX/UI Work)

We’re looking for a highly skilled UX/UI designer to translate our existing website design into an intuitive, beautiful mobile app interface for our Pellmoor-developed tele-wellness platform. Hoping this designer will stay onboard with us for future work.

Scope of Work:
    •    Review our existing website design (style, colors, typography, components)
    •    Apply the same visual language to our mobile app screens
    •    Ensure consistent, user-friendly experience across the app
    •    Deliver high-fidelity mockups and design assets (preferably in Figma)
    •    Minimal UX rethinking may be needed to optimize for mobile, but the core brand and design system are already established

What We Provide:
    •    Access to the existing website design (including any style guides or component libraries)
    •    Wireframes or a basic functional map of the app screens
    •    Clear guidelines on branding and user flows

Ideal Candidate:
    •    Strong portfolio of mobile app design, especially healthcare/wellness preferred
    •    Proven experience in adapting web designs for mobile apps
    •    Expertise with Figma or comparable tools
    •    Attention to detail and commitment to brand consistency
    •    Ability to deliver quickly while maintaining quality

Deliverables:
    •    Complete set of high-fidelity, mobile-optimized app screens
    •    Organized design file (Figma preferred) ready for developer handoff
    •    Design assets as needed (icons, images, components)

Timeline:
    •    Estimated 1 week for initial delivery, with room for revisions

```html
<!DOCTYPE html>
<html lang="en">
<head>
<meta charset="utf-8">
<title>Pellmoor Tele-Wellness App Screens</title>
<link href="https://fonts.googleapis.com/css2?family=Libre+Baskerville:wght@400;700&family=Poppins:wght@300;400;500&display=swap" rel="stylesheet">
<style>
:root{
  --page:#ececec;
  --screen:#f5f5f5;
  --white:#ffffff;
  --peach:#fde8d5;
  --peach-strong:#fdd5ac;
  --ink:#1f1f1f;
  --muted:#7a7a7a;
  --slot:#f3f3f3;
  --green-dark:#0f2a18;
  --green-mid:#2c5a35;
}
*{box-sizing:border-box;margin:0;padding:0}
html,body{width:1200px;height:1200px;overflow:hidden;background:var(--page)}
body{position:relative;font-family:"Poppins",sans-serif;color:var(--ink)}
.phone{position:absolute;top:181px;width:389px;height:838px;border-radius:46px;overflow:hidden}
.phone--home{left:176px;background:var(--screen)}
.phone--booking{left:636px;background:var(--peach)}
.abs{position:absolute}
.time{left:58px;top:15px;font-size:15px;font-weight:500}
.island{left:136px;top:10px;width:112px;height:33px;border-radius:17px;background:#000}
.status{left:273px;top:18px;display:flex;gap:6px;align-items:center}
.circle{border-radius:50%}
.serif{font-family:"Libre Baskerville",serif}
.avatar{background:linear-gradient(160deg,#cfd6e4,#8a6a5a)}
.icon-btn{width:43px;height:43px;background:var(--white);display:flex;align-items:center;justify-content:center}
.greeting{left:29px;top:138px;font-size:14px}
.headline{left:29px;top:162px;font-size:19.5px;letter-spacing:-.4px;white-space:nowrap}
.pill{height:50px;border-radius:25px;display:flex;align-items:center;justify-content:center;gap:9px;font-size:11.5px;font-weight:400;letter-spacing:.2px}
.pill--white{background:var(--white)}
.pill--peach{background:var(--peach-strong)}
.card{left:29px;width:330px;height:165px;border-radius:28px;overflow:hidden}
.card--appointment{top:302px;background:var(--peach);box-shadow:0 10px 20px rgba(240,200,160,.25)}
.card-title{font-size:13px;font-weight:700}
.doc-name{font-size:14.5px;font-weight:400;white-space:nowrap}
.doc-creds{font-size:10.5px;white-space:nowrap}
.cta{height:42px;border-radius:21px;background:var(--peach-strong);display:flex;align-items:center;justify-content:center;gap:6px;font-size:11.5px}
.card--tip{top:497px;background:radial-gradient(ellipse at 75% 40%,#6f8f72 0%,var(--green-mid) 30%,var(--green-dark) 75%)}
.tip-quote{left:0;width:330px;top:56px;text-align:center;color:#fff;font-size:17px;font-weight:300;line-height:27px}
.nav{left:0;top:745px;width:389px;height:93px;background:linear-gradient(rgba(255,255,255,.6),#fff)}
.nav-item{top:18px;width:90px;margin-left:-45px;text-align:center;font-size:10.5px;color:var(--muted)}
.nav-item svg{display:block;margin:0 auto 4px}
.nav-item--active{color:var(--ink)}
.home-bar{left:124px;top:824px;width:138px;height:4px;border-radius:2px;background:#000}
.month{left:29px;top:80px;font-size:21px;font-weight:700}
.day{width:50px;margin-left:-25px;text-align:center;font-size:12px;color:var(--muted)}
.day--active{color:var(--ink)}
.date-sel{left:73px;top:155px;width:42px;height:42px;background:var(--peach-strong)}
.sheet{left:0;top:214px;width:389px;height:624px;background:var(--white);border-radius:28px 28px 0 0}
.section{left:29px;top:45px;font-size:17.5px;font-weight:700}
.slot-time{left:36px;font-size:12px;color:var(--muted)}
.slot{left:29px;width:330px;height:71px;border-radius:26px;background:var(--slot)}
.slot--chosen{background:var(--peach);box-shadow:0 10px 18px rgba(240,200,160,.3)}
.footer-bar{left:29px;top:528px;width:337px;height:63px;border-radius:32px;background:var(--slot)}
</style>
</head>
<body>

<section class="phone phone--home">
  <div class="abs time">1:47</div>
  <div class="abs island"></div>
  <div class="abs status">
    <svg width="20" height="13" viewBox="0 0 20 13"><rect x="0" y="8" width="3.5" height="5" rx="1"/><rect x="5.5" y="5.5" width="3.5" height="7.5" rx="1"/><rect x="11" y="3" width="3.5" height="10" rx="1"/><rect x="16.5" y="0" width="3.5" height="13" rx="1"/></svg>
    <svg width="17" height="13" viewBox="0 0 17 13"><path d="M1 4.5a11 11 0 0 1 15 0M3.5 7.3a7.3 7.3 0 0 1 10 0M6 10a3.5 3.5 0 0 1 5 0" stroke="#000" stroke-width="2" fill="none" stroke-linecap="round"/><circle cx="8.5" cy="12" r="1.2"/></svg>
    <svg width="27" height="13" viewBox="0 0 27 13"><rect x=".5" y=".5" width="23" height="12" rx="3.5" fill="none" stroke="#999"/><rect x="2" y="2" width="20" height="9" rx="2"/><rect x="24.5" y="4" width="2" height="5" rx="1" fill="#999"/></svg>
  </div>

  <div class="abs circle avatar" style="left:29px;top:72px;width:43px;height:43px" role="img" aria-label="Profile photo of the member"></div>
  <div class="abs circle icon-btn" style="left:317px;top:72px">
    <svg width="20" height="20" viewBox="0 0 24 24" fill="none" stroke="#222" stroke-width="1.6" stroke-linecap="round"><path d="M6 16V11a6 6 0 0 1 12 0v5l1.5 2h-15z"/><path d="M10 20.5a2 2 0 0 0 4 0"/></svg>
  </div>
  <div class="abs circle" style="left:349px;top:72px;width:10px;height:10px;background:var(--peach-strong)"></div>

  <p class="abs greeting">Hello, Lena</p>
  <h1 class="abs headline serif" style="font-weight:400">Let’s optimize your wellness today.</h1>

  <div class="abs pill pill--white" style="left:29px;top:223px;width:186px">
    <svg width="20" height="20" viewBox="0 0 24 24" fill="none" stroke="#222" stroke-width="1.5" stroke-linecap="round"><rect x="3" y="5" width="18" height="16" rx="3"/><path d="M3 10h18M8 3v4M16 3v4M15 16h4M17 14v4"/></svg>
    BOOK CONSULTATION
  </div>
  <div class="abs pill pill--peach" style="left:230px;top:223px;width:129px">
    <svg width="21" height="16" viewBox="0 0 24 18" fill="none" stroke="#222" stroke-width="1.5" stroke-linejoin="round"><rect x="1" y="2" width="15" height="14" rx="3"/><path d="M16 7l6-3v10l-6-3"/></svg>
    VIDEO CALL
  </div>

  <div class="abs card card--appointment">
    <svg class="abs" style="left:17px;top:19px" width="20" height="20" viewBox="0 0 24 24" fill="none" stroke="#222" stroke-width="1.5" stroke-linecap="round"><path d="M4 3v6a5 5 0 0 0 10 0V3M9 14v2a4 4 0 0 0 8 0v-3"/><circle cx="17" cy="10" r="2.5"/></svg>
    <h2 class="abs card-title serif" style="left:50px;top:21px">Next Appointment</h2>
    <svg class="abs" style="left:298px;top:21px" width="8" height="16" viewBox="0 0 8 16" fill="none" stroke="#222" stroke-width="1.4"><circle cx="4" cy="3" r="2"/><circle cx="4" cy="12" r="2"/></svg>
    <div class="abs circle avatar" style="left:14px;top:58px;width:42px;height:42px" role="img" aria-label="Doctor portrait"></div>
    <p class="abs doc-name" style="left:65px;top:61px">Dr. Clara Voss</p>
    <p class="abs doc-creds" style="left:65px;top:82px">MBBS, BAMS, Oncology Director</p>
    <div class="abs circle icon-btn" style="left:14px;top:109px;width:42px;height:42px;background:#fdf1e6">
      <svg width="20" height="20" viewBox="0 0 24 24" fill="none" stroke="#222" stroke-width="1.5" stroke-linecap="round"><rect x="3" y="5" width="18" height="16" rx="3"/><path d="M3 10h18M8 3v4M16 3v4M15 16h4M17 14v4"/></svg>
    </div>
    <p class="abs" style="left:65px;top:120px;font-size:12.5px">July 12, 2:00 PM</p>
    <div class="abs cta" style="left:216px;top:115px;width:107px">JOIN NOW
      <svg width="14" height="10" viewBox="0 0 14 10" fill="none" stroke="#222" stroke-width="1.4" stroke-linecap="round"><path d="M1 5h12M9 1l4 4-4 4"/></svg>
    </div>
  </div>

  <div class="abs card card--tip" role="img" aria-label="Photo of white bell-shaped flowers on green leaves">
    <svg class="abs" style="left:17px;top:19px" width="22" height="22" viewBox="0 0 24 24" fill="none" stroke="#fff" stroke-width="1.5" stroke-linecap="round"><path d="M9 17h6M10 20h4M8 13a5 5 0 1 1 8 0c-1 1-1 2-1 4H9c0-2 0-3-1-4z"/><path d="M12 1v2M3 9h2M19 9h2M5 3l1.5 1.5M19 3l-1.5 1.5"/></svg>
    <h2 class="abs card-title serif" style="left:57px;top:22px;color:#fff">Wellness Tip</h2>
    <svg class="abs" style="left:293px;top:20px" width="18" height="18" viewBox="0 0 24 24" fill="none" stroke="#fff" stroke-width="1.6"><circle cx="18" cy="5" r="3"/><circle cx="6" cy="12" r="3"/><circle cx="18" cy="19" r="3"/><path d="M8.6 10.5l6.8-4M8.6 13.5l6.8 4"/></svg>
    <p class="abs tip-quote">"Stay hydrated!<br>Drink 2L water today."</p>
    <div class="abs cta" style="left:209px;top:115px;width:114px">LEARN MORE
      <svg width="14" height="10" viewBox="0 0 14 10" fill="none" stroke="#222" stroke-width="1.4" stroke-linecap="round"><path d="M1 5h12M9 1l4 4-4 4"/></svg>
    </div>
  </div>

  <div class="abs circle icon-btn" style="left:29px;top:691px;background:#f0f0f0">
    <svg width="20" height="20" viewBox="0 0 24 24" fill="none" stroke="#222" stroke-width="1.5" stroke-linecap="round"><path d="M4 20C4 10 10 5 20 4c0 10-5 16-14 15M4 20l9-9"/></svg>
  </div>
  <h2 class="abs card-title serif" style="left:78px;top:705px">Your Care Team</h2>

  <nav class="abs nav">
    <div class="abs nav-item nav-item--active" style="left:59px">
      <svg width="18" height="18" viewBox="0 0 24 24"><path d="M3 10l9-7 9 7v9a3 3 0 0 1-3 3H6a3 3 0 0 1-3-3z" fill="#333"/><path d="M12 10v7M8.5 13.5h7" stroke="#fff" stroke-width="1.8" stroke-linecap="round"/></svg>My Home</div>
    <div class="abs nav-item" style="left:148px">
      <svg width="18" height="18" viewBox="0 0 24 24" fill="none" stroke="#888" stroke-width="1.5" stroke-linecap="round"><path d="M4 20C4 10 10 5 20 4c0 10-5 16-14 15M4 20l9-9"/></svg>My Care</div>
    <div class="abs nav-item" style="left:240px">
      <svg width="18" height="18" viewBox="0 0 24 24" fill="none" stroke="#888" stroke-width="1.5" stroke-linecap="round"><path d="M4 3v6a5 5 0 0 0 10 0V3M9 14v2a4 4 0 0 0 8 0v-3"/><circle cx="17" cy="10" r="2.5"/></svg>My Checkups</div>
    <div class="abs nav-item" style="left:328px">
      <svg width="20" height="18" viewBox="0 0 24 22" fill="none" stroke="#888" stroke-width="1.5" stroke-linejoin="round"><path d="M3 3h18v12H10l-5 4v-4H3z"/><circle cx="8" cy="9" r=".6" fill="#888"/><circle cx="12" cy="9" r=".6" fill="#888"/><circle cx="16" cy="9" r=".6" fill="#888"/></svg>My Texts</div>
  </nav>
  <div class="abs home-bar"></div>
</section>

<section class="phone phone--booking">
  <div class="abs time">1:47</div>
  <div class="abs island"></div>
  <div class="abs status">
    <svg width="20" height="13" viewBox="0 0 20 13"><rect x="0" y="8" width="3.5" height="5" rx="1"/><rect x="5.5" y="5.5" width="3.5" height="7.5" rx="1"/><rect x="11" y="3" width="3.5" height="10" rx="1"/><rect x="16.5" y="0" width="3.5" height="13" rx="1"/></svg>
    <svg width="17" height="13" viewBox="0 0 17 13"><path d="M1 4.5a11 11 0 0 1 15 0M3.5 7.3a7.3 7.3 0 0 1 10 0M6 10a3.5 3.5 0 0 1 5 0" stroke="#000" stroke-width="2" fill="none" stroke-linecap="round"/><circle cx="8.5" cy="12" r="1.2"/></svg>
    <svg width="27" height="13" viewBox="0 0 27 13"><rect x=".5" y=".5" width="23" height="12" rx="3.5" fill="none" stroke="#999"/><rect x="2" y="2" width="20" height="9" rx="2"/><rect x="24.5" y="4" width="2" height="5" rx="1" fill="#999"/></svg>
  </div>

  <h1 class="abs month serif">May, 2025</h1>
  <div class="abs circle icon-btn" style="left:317px;top:72px;background:#fdf1e6">
    <svg width="21" height="21" viewBox="0 0 24 24" fill="none" stroke="#222" stroke-width="1.5" stroke-linecap="round"><rect x="3" y="5" width="18" height="16" rx="3"/><path d="M3 10h18M8 3v4M16 3v4"/><circle cx="15.5" cy="15.5" r="1.8"/></svg>
  </div>

  <div class="abs day" style="left:42px;top:132px">SUN</div>
  <div class="abs day day--active" style="left:94px;top:132px">MON</div>
  <div class="abs day" style="left:146px;top:132px">TUE</div>
  <div class="abs day" style="left:194px;top:132px">WED</div>
  <div class="abs day" style="left:243px;top:132px">FRI</div>
  <div class="abs day" style="left:294px;top:132px">SAT</div>
  <div class="abs day" style="left:347px;top:132px">SUN</div>
  <div class="abs circle date-sel"></div>
  <div class="abs day" style="left:42px;top:167px">01</div>
  <div class="abs day day--active" style="left:94px;top:167px">02</div>
  <div class="abs day" style="left:146px;top:167px">03</div>
  <div class="abs day" style="left:194px;top:167px">04</div>
  <div class="abs day" style="left:243px;top:167px">05</div>
  <div class="abs day" style="left:294px;top:167px">06</div>
  <div class="abs day" style="left:347px;top:167px">07</div>

  <div class="abs sheet">
    <h2 class="abs section serif">Available Openings</h2>

    <p class="abs slot-time" style="top:83px">11:00 AM</p>
    <div class="abs slot" style="top:103px">
      <div class="abs circle avatar" style="left:14px;top:14px;width:42px;height:42px" role="img" aria-label="Doctor portrait"></div>
      <p class="abs doc-name" style="left:65px;top:18px">Dr. Clara Voss</p>
      <p class="abs doc-creds" style="left:65px;top:40px">MBBS, BAMS, Oncology Director</p>
    </div>

    <div class="abs slot slot--chosen" style="top:188px">
      <div class="abs circle avatar" style="left:14px;top:14px;width:42px;height:42px" role="img" aria-label="Doctor portrait"></div>
      <p class="abs doc-name" style="left:65px;top:18px">Dr. Nina Hale</p>
      <p class="abs doc-creds" style="left:65px;top:40px">MBBS, BAMS, OBGYN and Women's health</p>
      <div class="abs circle" style="left:288px;top:15px;width:28px;height:28px;background:#fef3e8;display:flex;align-items:center;justify-content:center">
        <svg width="13" height="10" viewBox="0 0 13 10" fill="none" stroke="#222" stroke-width="1.5" stroke-linecap="round"><path d="M1 5l4 4 7-8"/></svg>
      </div>
    </div>

    <p class="abs slot-time" style="top:283px">01:30 PM</p>
    <div class="abs slot" style="top:303px">
      <div class="abs circle avatar" style="left:14px;top:14px;width:42px;height:42px" role="img" aria-label="Doctor portrait"></div>
      <p class="abs doc-name" style="left:65px;top:18px">Dr. Clara Voss</p>
      <p class="abs doc-creds" style="left:65px;top:40px">MBBS, BAMS, Oncology Director</p>
    </div>

    <div class="abs footer-bar">
      <svg class="abs" style="left:21px;top:26px" width="15" height="11" viewBox="0 0 15 11" fill="none" stroke="#222" stroke-width="1.4" stroke-linecap="round"><path d="M14 5.5H1M5 1.5l-4 4 4 4"/></svg>
      <p class="abs" style="left:51px;top:13px;font-size:9.5px;color:var(--muted)">SPECIALTY:</p>
      <p class="abs" style="left:51px;top:31px;font-size:12px">WOMEN'S HEALTH</p>
      <div class="abs cta" style="left:209px;top:7px;width:122px;height:50px;border-radius:25px">BOOK NOW
        <svg width="13" height="10" viewBox="0 0 13 10" fill="none" stroke="#222" stroke-width="1.5" stroke-linecap="round"><path d="M1 5l4 4 7-8"/></svg>
      </div>
    </div>
  </div>
  <div class="abs home-bar"></div>
</section>

</body>
</html>
```